Business cards

We need business cards for the logo that you designed for our company. Something simple and clean.

Target Market(s)

Homeowners/ people looking for construction work

Industry/Entity Type

Construction

Contact Information for Business Card

Name: Doug Whitby, Number: 602-555-0174, Email: WhitbyBuildingCompany@mailbox-example.net ROC# 482063

Font styles to use
Serif

Colors

Designer to choose colors to be used in the design.

Requirements
Must have
• On one side of the card I would like to be all of the personal information I have put above along with the company logo that I have attached.
• On the other side of the card I would like the top half of the card to be the logo and then on the bottom half I would like to have the areas of construction we focus on along with an icon that represents it like the picture I have attached.
• Areas we focus on:
• Roofing, Kitchen and bath Remodel, Water Damage, Storm Damage, Fire Damage, Insurance Specialist
• If we could arrange those in alphabetical order.
Nice to have
• I have added 2 company logos a colorful one and a black one it would be nice to see a couple different options the black logo to be more simple and sleek and the colorful logo to be more colorful

```html
<!DOCTYPE html>
<html lang="en">
<head>
<meta charset="utf-8">
<title>Whitby Building Company – Business Cards</title>
<link rel="stylesheet" href="https://fonts.googleapis.com/css2?family=Arimo:wght@400;700&family=Lato:wght@400;700&display=swap">
<style>
  :root {
    --backdrop: #8a5a36;
    --kraft-light: #d2ad7e;
    --kraft: #c69a68;
    --kraft-dark: #b98c5c;
    --ink: #111111;
    --icon-fg: #ffffff;
  }
  * { margin: 0; padding: 0; box-sizing: border-box; }
  html, body { width: 1200px; height: 900px; overflow: hidden; }
  body {
    position: relative;
    background: var(--backdrop);
    color: var(--ink);
    font-family: "Arimo", Arial, sans-serif;
  }
  .card {
    position: absolute;
    left: 330px;
    width: 556px;
    height: 343px;
    background: linear-gradient(160deg, var(--kraft-light) 0%, var(--kraft) 45%, var(--kraft-dark) 100%);
  }
  .card--front { top: 90px; }
  .card--back { top: 470px; }

  /* Front */
  .brand {
    position: absolute;
    top: 72px;
    left: 0;
    width: 100%;
    display: flex;
    align-items: center;
    justify-content: center;
    gap: 12px;
  }
  .brand__mark { width: 26px; height: 26px; background: var(--ink); }
  .brand__name {
    font-family: "Arimo", Arial, sans-serif;
    font-weight: 700;
    font-size: 26px;
    letter-spacing: 1px;
    text-transform: uppercase;
  }
  .person {
    position: absolute;
    top: 164px;
    width: 100%;
    text-align: center;
    font-weight: 700;
    font-size: 21px;
    text-transform: uppercase;
  }
  .rule {
    position: absolute;
    left: 132px;
    width: 290px;
    height: 1px;
    background: var(--ink);
  }
  .rule--top { top: 201px; }
  .rule--bottom { top: 275px; }
  .contact {
    position: absolute;
    top: 218px;
    width: 100%;
    text-align: center;
    font-size: 15px;
    line-height: 21px;
  }
  .license {
    position: absolute;
    top: 289px;
    width: 100%;
    text-align: center;
    font-size: 15px;
  }

  /* Back */
  .services {
    position: absolute;
    inset: 0;
    list-style: none;
  }
  .service {
    position: absolute;
    width: 180px;
    margin-left: -90px;
    text-align: center;
    font-family: "Lato", Arial, sans-serif;
    font-weight: 700;
    font-size: 12.5px;
    line-height: 16px;
    text-transform: uppercase;
  }
  .service__icon { display: block; width: 76px; height: 76px; margin: 0 auto 6px; }
  .col-1 { left: 89px; } .col-2 { left: 278px; } .col-3 { left: 451px; }
  .row-1 { top: 50px; } .row-2 { top: 198px; }
</style>
</head>
<body>

<section class="card card--front" aria-label="Business card front">
  <div class="brand">
    <span class="brand__mark"></span>
    <span class="brand__name">Whitby Building Company</span>
  </div>
  <h1 class="person">Doug Whitby</h1>
  <div class="rule rule--top"></div>
  <p class="contact">602-555-0174<br>WhitbyBuildingCompany@mailbox-example.net</p>
  <div class="rule rule--bottom"></div>
  <p class="license">ROC# 482063</p>
</section>

<section class="card card--back" aria-label="Business card back">
  <ul class="services">
    <li class="service col-1 row-1">
      <svg class="service__icon" viewBox="0 0 76 76" aria-hidden="true">
        <rect width="76" height="76" rx="8" fill="#111"/>
        <path d="M38 16c2 9 12 13 12 26a12 12 0 0 1-24 0c0-6 3-9 5-12 0 5 3 7 4 7-2-7 1-15 3-21z" fill="#fff"/>
        <path d="M38 40c3 4 5 6 5 10a5 5 0 0 1-10 0c0-3 2-6 5-10z" fill="#111"/>
      </svg>
      Fire Damage
    </li>
    <li class="service col-2 row-1">
      <svg class="service__icon" viewBox="0 0 76 76" aria-hidden="true">
        <rect width="76" height="76" rx="8" fill="#111"/>
        <path d="M38 14 22 28h4v14h24V28h4z" fill="#fff"/>
        <rect x="34" y="32" width="8" height="10" fill="#111"/>
        <path d="M14 38c0 10 6 18 16 22l4-6c-6-2-10-7-12-14z" fill="#fff"/>
        <path d="M62 38c0 10-6 18-16 22l-4-6c6-2 10-7 12-14z" fill="#fff"/>
      </svg>
      Insurance Specialist
    </li>
    <li class="service col-3 row-1">
      <svg class="service__icon" viewBox="0 0 76 76" aria-hidden="true">
        <rect width="76" height="76" rx="8" fill="#111"/>
        <path d="M46 40V18h10" stroke="#fff" stroke-width="3" fill="none"/>
        <path d="M52 20h10l-2 5h-6z" fill="#fff"/>
        <g fill="#fff"><circle cx="54" cy="29" r="1.3"/><circle cx="58" cy="29" r="1.3"/><circle cx="56" cy="33" r="1.3"/></g>
        <rect x="12" y="40" width="52" height="5" rx="2" fill="#fff"/>
        <path d="M15 46h46c0 8-5 12-12 12H27c-7 0-12-4-12-12z" fill="#fff"/>
        <rect x="20" y="57" width="4" height="5" fill="#fff"/><rect x="52" y="57" width="4" height="5" fill="#fff"/>
      </svg>
      Kitchen &amp;<br>Bath Remodel
    </li>
    <li class="service col-1 row-2">
      <svg class="service__icon" viewBox="0 0 76 76" aria-hidden="true">
        <rect width="76" height="76" rx="8" fill="#111"/>
        <path d="M14 54 32 22h18l14 32z" fill="#fff"/>
        <g stroke="#111" stroke-width="2.5"><path d="M22 54 38 24"/><path d="M29 54 44 24"/><path d="M36 54 50 26"/></g>
        <rect x="48" y="44" width="8" height="10" fill="#111"/>
      </svg>
      Roofing
    </li>
    <li class="service col-2 row-2">
      <svg class="service__icon" viewBox="0 0 76 76" aria-hidden="true">
        <rect width="76" height="76" rx="8" fill="#111"/>
        <path d="M24 46a10 10 0 0 1 0-20 14 14 0 0 1 27-2 11 11 0 0 1 2 22" fill="none" stroke="#fff" stroke-width="3"/>
        <path d="M40 34l-8 14h6l-4 12 10-16h-6l4-10z" fill="#fff"/>
      </svg>
      Storm Damage
    </li>
    <li class="service col-3 row-2">
      <svg class="service__icon" viewBox="0 0 76 76" aria-hidden="true">
        <rect width="76" height="76" rx="8" fill="#111"/>
        <path d="M38 14c6 10 12 17 12 25a12 12 0 0 1-24 0c0-8 6-15 12-25z" fill="#fff"/>
        <path d="M14 52c6 0 10 2 14 6-6-1-11-2-14-6zM62 52c-6 0-10 2-14 6 6-1 11-2 14-6z" fill="#fff"/>
        <circle cx="18" cy="44" r="2.5" fill="#fff"/><circle cx="58" cy="44" r="2.5" fill="#fff"/>
      </svg>
      Water Damage
    </li>
  </ul>
</section>

</body>
</html>
```